Quarvolindex Website

we need a web site similar to Pluvrex.com or Zantor7 com or halverpoint.com - Although our budget is small we would like to look like them. we are in the same industry
Updates
Reason: Can you do an exact copy of Pluvrex.com if so how long ? What do you require? What is the next step?Please let me know you can also email me at dorvilak@quenmoxa.com for faster answers.
Thank you
Target Market(s)
small and medium size business
Requirements
Must have
- product portfolio - just like Pluvrex.com
Nice to have
- ecomerce and mobile app

```html
<!DOCTYPE html>
<html lang="en">
<head>
<meta charset="utf-8">
<title>Quarvolindex</title>
<link href="https://fonts.googleapis.com/css2?family=Source+Sans+3:wght@300;400;600;700&display=swap" rel="stylesheet">
<style>
:root{
  --blue:#0f6fd8;
  --footer:#3c9ae8;
  --ink:#3a3a3a;
  --muted:#6b6b6b;
  --rule:#d8d8d8;
  --dark:#2d2d2d;
}
*{box-sizing:border-box;margin:0;padding:0}
html,body{width:890px;height:1200px;overflow:hidden}
body{font-family:"Source Sans 3",sans-serif;color:var(--ink);background:#fff;position:relative}
.abs{position:absolute}
/* header */
.header{position:absolute;left:0;top:0;width:890px;height:81px;background:#fff}
.brand{position:absolute;left:96px;top:36px;display:flex;align-items:center;gap:8px}
.brand-dot{width:20px;height:20px;border-radius:50%;background:var(--blue)}
.brand-name{font-size:25px;font-weight:700;color:var(--blue);letter-spacing:.2px}
.nav{position:absolute;right:98px;top:44px;display:flex;font-size:12px;color:var(--dark)}
.nav span{padding:0 12px}
.nav .sep{padding:0}
/* hero */
.hero{position:absolute;left:0;top:81px;width:890px;height:322px;
  background:linear-gradient(90deg,#e6e9ef 0%,#b9c3d6 45%,#4a5a7c 70%,#2a3656 100%)}
.hero-panel{position:absolute;left:96px;top:109px;width:340px;height:140px;background:rgba(20,108,220,.88);color:#fff;padding:14px 20px}
.hero-panel h1{font-weight:300;font-size:25px;margin-bottom:12px}
.hero-panel p{font-size:9px;line-height:17.5px;font-weight:400;letter-spacing:-.1px}
.hero-arrows{position:absolute;left:94px;top:261px;display:flex;gap:3px}
.arrow{width:22px;height:22px;border-radius:50%;background:var(--dark);display:flex;align-items:center;justify-content:center}
.arrow.sm{width:18px;height:18px}
/* services */
.services{position:absolute;left:0;top:403px;width:890px;height:271px;background:linear-gradient(#fff,#e7e7e8)}
.service{position:absolute;top:40px;width:170px;text-align:center}
.service .ring{width:98px;height:98px;border-radius:50%;background:var(--blue);margin:0 auto;display:flex;align-items:center;justify-content:center}
.service h2{font-size:15px;font-weight:600;color:#555;margin-top:12px}
.service p{font-size:11.5px;font-weight:300;line-height:18px;color:var(--muted);margin-top:10px}
/* columns */
.col{position:absolute;top:695px;width:226px}
.col h3{font-size:15px;font-weight:600;color:#555;height:30px;line-height:30px}
.col .ctrl{position:absolute;right:0;top:6px;display:flex;gap:2px}
.vrule{position:absolute;top:694px;width:1px;height:224px;background:#e2e2e2}
.news{position:absolute;left:0;display:flex;gap:15px}
.thumb{width:65px;height:57px;flex:none}
.news h4{font-size:11.5px;font-weight:600;color:#444;white-space:nowrap}
.news p{font-size:9px;line-height:15px;color:var(--muted);margin-top:2px}
.small-h{font-size:11.5px;font-weight:600;color:#444}
.body-txt{font-size:9px;line-height:15px;color:var(--muted);text-align:justify}
/* footer */
.footer{position:absolute;left:0;top:948px;width:890px;height:252px;background:var(--footer);color:#fff}
.fcol{position:absolute;top:27px}
.fcol h5{font-size:11.5px;font-weight:600;margin-bottom:11px}
.fcol li{list-style:none;font-size:9px;line-height:22.4px}
.field{width:164px;height:20px;background:#fff;border:1px solid #cfd8e2;font-size:8.5px;color:#aaa;padding:4px 10px;margin-top:10px}
.subscribe{position:absolute;left:92px;top:153px;width:73px;height:17px;border-radius:9px;background:var(--dark);font-size:9.5px;text-align:center;line-height:17px}
.social{display:flex;align-items:center;justify-content:space-between;width:106px;height:28px;font-size:11px}
.social i{width:20px;height:20px;border-radius:50%;background:#fff;display:block}
.frule{position:absolute;left:8px;top:187px;width:874px;height:1px;background:rgba(255,255,255,.25)}
.copy{position:absolute;left:0;width:890px;top:210px;text-align:center;font-size:11px;letter-spacing:-.3px}
</style>
</head>
<body>

<header class="header">
  <div class="brand"><span class="brand-dot"></span><span class="brand-name">QUARVOLINDEX</span></div>
  <nav class="nav"><span>Home</span><span class="sep">|</span><span>About Us</span><span class="sep">|</span><span>Services</span><span class="sep">|</span><span>FAQ's</span><span class="sep">|</span><span>Contact Us</span></nav>
</header>

<section class="hero" role="img" aria-label="Photo of a businessman in a suit touching an outlined cloud on a glass screen">
  <div class="hero-panel">
    <h1>Quarvolindex</h1>
    <p>&nbsp;It has survived not only five centuries, but also the leap into electronic typeset-ting, remaining essentially unchanged. It was popularised in the 1960s with the release of Kelvane sheets containing Lorem Ipsum passages, and more recently with desktop publishing software like Brisk Pagesetter</p>
  </div>
  <div class="hero-arrows">
    <span class="arrow"><svg width="10" height="10" viewBox="0 0 10 10"><path d="M6.5 1.5 3 5l3.5 3.5" fill="none" stroke="#fff" stroke-width="1.8"/></svg></span>
    <span class="arrow"><svg width="10" height="10" viewBox="0 0 10 10"><path d="M3.5 1.5 7 5 3.5 8.5" fill="none" stroke="#fff" stroke-width="1.8"/></svg></span>
  </div>
</section>

<section class="services">
  <div class="service" style="left:93px">
    <div class="ring"><svg width="40" height="34" viewBox="0 0 40 34" fill="#fff"><rect x="2" y="2" width="36" height="8" rx="2"/><rect x="2" y="13" width="36" height="8" rx="2"/><rect x="2" y="24" width="36" height="8" rx="2"/><circle cx="32" cy="6" r="1.5" fill="#0f6fd8"/><circle cx="32" cy="17" r="1.5" fill="#0f6fd8"/><circle cx="32" cy="28" r="1.5" fill="#0f6fd8"/></svg></div>
    <h2>Cloud</h2>
    <p>Lorem Ipsum is simply dummy text of the printing and typesetting industry. Lorem Ipsum ...</p>
  </div>
  <div class="service" style="left:271px">
    <div class="ring"><svg width="26" height="42" viewBox="0 0 26 42"><rect x="1" y="1" width="24" height="40" rx="3" fill="#fff"/><rect x="4" y="6" width="18" height="26" fill="#0f6fd8"/><circle cx="13" cy="36.5" r="2" fill="#0f6fd8"/></svg></div>
    <h2>Mobile</h2>
    <p>Lorem Ipsum is simply dummy text of the printing and typesetting industry. Lorem Ipsum ...</p>
  </div>
  <div class="service" style="left:449px">
    <div class="ring"><svg width="36" height="42" viewBox="0 0 36 42" fill="#fff"><rect x="1" y="1" width="9" height="40" rx="3"/><rect x="12" y="4" width="23" height="37" rx="2"/><rect x="15" y="8" width="17" height="8" fill="#0f6fd8"/><g fill="#0f6fd8"><rect x="15" y="20" width="4" height="3"/><rect x="21.5" y="20" width="4" height="3"/><rect x="28" y="20" width="4" height="3"/><rect x="15" y="26" width="4" height="3"/><rect x="21.5" y="26" width="4" height="3"/><rect x="28" y="26" width="4" height="3"/><rect x="15" y="32" width="4" height="3"/><rect x="21.5" y="32" width="4" height="3"/><rect x="28" y="32" width="4" height="3"/></g></svg></div>
    <h2>Landline</h2>
    <p>Lorem Ipsum is simply dummy text of the printing and typesetting industry. Lorem Ipsum ...</p>
  </div>
  <div class="service" style="left:627px">
    <div class="ring"><svg width="38" height="38" viewBox="0 0 38 38" fill="none" stroke="#fff" stroke-width="2.6"><circle cx="19" cy="19" r="17"/><ellipse cx="19" cy="19" rx="7" ry="17"/><path d="M2 19h34M5 10h28M5 28h28M19 2v34"/></svg></div>
    <h2>Network</h2>
    <p>Lorem Ipsum is simply dummy text of the printing and typesetting industry. Lorem Ipsum ...</p>
  </div>
</section>

<section class="col" style="left:95px">
  <h3>Latest News</h3>
  <div class="ctrl">
    <span class="arrow sm"><svg width="8" height="8" viewBox="0 0 10 10"><path d="M6.5 1.5 3 5l3.5 3.5" fill="none" stroke="#fff" stroke-width="2"/></svg></span>
    <span class="arrow sm"><svg width="8" height="8" viewBox="0 0 10 10"><path d="M3.5 1.5 7 5 3.5 8.5" fill="none" stroke="#fff" stroke-width="2"/></svg></span>
  </div>
  <div class="news" style="top:50px">
    <div class="thumb" role="img" aria-label="Blue digital circuit illustration" style="background:linear-gradient(135deg,#0a2a78,#1c6ad8 55,#0b2f86);background:linear-gradient(135deg,#0a2a78,#1c6ad8,#0b2f86)"></div>
    <div><h4>Lorem Ipsum is simply dummy</h4><p>Text of the printing and typesetting industry. Lorem Ipsum has been the industry's standard dummy text</p></div>
  </div>
  <div class="news" style="top:142px">
    <div class="thumb" role="img" aria-label="Blue network cable illustration" style="background:linear-gradient(135deg,#0c3f9a,#3a86dd,#0a2f7c)"></div>
    <div><h4>Lorem Ipsum is simply dummy</h4><p>Text of the printing and typesetting industry. Lorem Ipsum has been the industry's standard dummy text</p></div>
  </div>
</section>
<div class="vrule" style="left:325px"></div>

<section class="col" style="left:333px;width:222px">
  <h3>Customer Testimonials</h3>
  <div class="ctrl">
    <span class="arrow sm"><svg width="8" height="8" viewBox="0 0 10 10"><path d="M6.5 1.5 3 5l3.5 3.5" fill="none" stroke="#fff" stroke-width="2"/></svg></span>
    <span class="arrow sm"><svg width="8" height="8" viewBox="0 0 10 10"><path d="M3.5 1.5 7 5 3.5 8.5" fill="none" stroke="#fff" stroke-width="2"/></svg></span>
  </div>
  <div class="abs" style="left:0;top:50px;width:64px;height:57px;background:linear-gradient(#6a5a4e,#2e2a2c)" role="img" aria-label="Portrait of the customer"></div>
  <div class="abs" style="left:78px;top:58px"><div class="small-h">Harlan Vestrow</div><div style="font-size:9px;color:var(--muted);margin-top:2px">CEO Cloud Technology</div></div>
  <div class="abs small-h" style="left:0;top:131px">A Good Experience</div>
  <p class="abs body-txt" style="left:0;top:155px;width:222px">Lorem Ipsum is simply dummy text of the printing and typesetting industry. Lorem Ipsum has been the industry's standard dummy text ever since the 1500s ...</p>
</section>
<div class="vrule" style="left:563px"></div>

<section class="col" style="left:570px;width:223px">
  <h3 style="line-height:27px">Cloud Technology</h3>
  <div class="ctrl">
    <span class="arrow sm"><svg width="8" height="8" viewBox="0 0 10 10"><path d="M6.5 1.5 3 5l3.5 3.5" fill="none" stroke="#fff" stroke-width="2"/></svg></span>
    <span class="arrow sm"><svg width="8" height="8" viewBox="0 0 10 10"><path d="M3.5 1.5 7 5 3.5 8.5" fill="none" stroke="#fff" stroke-width="2"/></svg></span>
  </div>
  <div class="abs small-h" style="left:0;top:48px">Our Services</div>
  <p class="abs body-txt" style="left:0;top:72px;width:223px">Lorem Ipsum is simply dummy text of the printing and typesetting industry. Lorem Ipsum has been the industry's standard dummy text ever since the 1500s It has survived not only five centuries, but also the leap into electronic typesetting, remaining essentially unchanged. It was popularised in the 1960s with the release of Kelvane sheets containing Lorem Ipsum passages, and more recently with desktop publishing software .</p>
</section>

<footer class="footer">
  <div class="fcol" style="left:100px"><h5>Quick Links</h5><ul><li>Home</li><li>About Us</li><li>Services</li><li>FAQ's</li><li>Contact Us</li></ul></div>
  <div class="fcol" style="left:279px"><h5>Support Links</h5><ul><li>Legal Notice</li><li>Privacy Policy</li><li>Terms &amp; Conditions</li><li>Help</li></ul></div>
  <div class="fcol" style="left:458px;width:166px;height:180px">
    <h5>Newsletter SignUp</h5>
    <p style="font-size:9px;line-height:18px">Sign-up for our daily emails by entering your information below:</p>
    <div class="field">Name</div>
    <div class="field">Enter Your E-Mail ID</div>
    <div class="subscribe">Subscribe</div>
  </div>
  <div class="fcol" style="left:694px">
    <h5>Connect With Us</h5>
    <div class="social"><i></i><span>Chirpwell</span></div>
    <div class="social"><i></i><span>Faceloop</span></div>
    <div class="social"><i></i><span>Linkmesh</span></div>
  </div>
  <div class="frule"></div>
  <div class="copy">Copyright©2013 Company Name &nbsp;- All rights reserved</div>
</footer>

</body>
</html>
```